Data Flow Illustrative Diagram

We'd like an illustrative diagram for a data product we are developing. The product is based in the construction industry and is a rating system for contractros.
We want to illustrate a number of states in the process.
1. Data Collection
- We have an online interface in which contractors can upload their data in multiple formats.
- Data is also collected from third party data feeds
- All Data is stored in a centralized database
2. Data Cleansing and Merging
- The collected data from all sources is cleansed and merged together
- Need to highlight that this data is secure and never shared
3. Data Prep/Ratio Calculation
- The data is then manipulated to show and prepared for a run through a financial model
- Again, need to indicate that the orginal RAW data collected in 1 and 2 is never shared
4. Model Run / Scoring
We run financial models on the data produced in Stage 3 to generate a "score/grade" for the individual contractors
5a. Dashboard - Paying Users
The contractor "score/grade" from 4 is available on a dashboard for paying users to see
5b. Dashboard - contractors
The contractor can also log into a dashboard to see their individual score along with where they rank amongst other contractors.
6. We gather contractor project review information and feed it into the model the the Dashboard/interface
7. Machine Learning / Artificial Intelligence
- We need another component off of Stage 3/4 that indicates we are running machine learning algorithms on the data to produce constantly improving results.
This illustrative diagram will be shown to contractors as well as technical companies so it should be clear and easy to understand.
Our website/company colours are purple (accented with blue).
See the two attached diagrams for very basic ideas of the flow. We'd like something much more polished and professional but extremely easy to understand.
Extending the deadline and guaranteeing the project.
- Please note that I'm looking to show a flow of data moving through a system. Not simply an itemized list
- This is in the construction industry and should reflect that.
- IMPORTANT TO HIGHLIGHT: This is a centralized database for the industry. Data is collected from multiple sources and stored in a secure central location.
Construction Industry
Construction

```html
<!DOCTYPE html>
<html lang="en">
<head>
<meta charset="utf-8">
<title>Data Flow Chart</title>
<link rel="stylesheet" href="https://fonts.googleapis.com/css2?family=Open+Sans:wght@400;600&display=swap">
<style>
  :root {
    --purple: #6b3fa0;
    --purple-dark: #4d2a7c;
    --purple-soft: #8a66bb;
    --blue: #37a9dd;
    --blue-dark: #1f86bf;
    --ink: #222222;
    --grey-star: #d3d3d3;
    --paper: #ffffff;
  }
  html, body {
    margin: 0;
    padding: 0;
    width: 1200px;
    height: 771px;
    overflow: hidden;
    background: var(--paper);
  }
  .chart {
    display: block;
    width: 1200px;
    height: 771px;
    font-family: "Open Sans", Arial, sans-serif;
  }
  .chart-title { fill: var(--purple); font-size: 50px; font-weight: 400; }
  .title-rule { stroke: var(--blue); stroke-width: 3; }
  .label { fill: var(--ink); font-size: 15px; }
  .caption { fill: var(--ink); font-size: 13.5px; }
  .step-num { fill: var(--blue); font-weight: 600; }
  .flow-dash { stroke: var(--ink); stroke-width: 2.2; stroke-dasharray: 6 4; fill: none; }
  .flow-solid { stroke: var(--ink); stroke-width: 1; fill: none; }
  .ml-frame { stroke: var(--blue); stroke-width: 3; stroke-dasharray: 7 5; fill: none; }
  .fill-purple { fill: var(--purple); }
  .fill-blue { fill: var(--blue); }
  .stroke-blue { stroke: var(--blue); fill: none; }
  .stroke-purple { stroke: var(--purple); fill: none; }
  .star-on { fill: var(--blue); }
  .star-off { fill: var(--grey-star); }
  .doc-line { stroke: var(--purple-soft); stroke-width: 4; }
</style>
</head>
<body>
<svg class="chart" viewBox="0 0 1200 771" xmlns="http://www.w3.org/2000/svg">
  <defs>
    <marker id="chevron" viewBox="0 0 12 12" refX="9" refY="6" markerWidth="9" markerHeight="9" orient="auto-start-reverse" markerUnits="userSpaceOnUse">
      <path d="M2 1 L9 6 L2 11" fill="none" stroke="#222" stroke-width="2.4"/>
    </marker>
    <marker id="tip" viewBox="0 0 10 10" refX="9" refY="5" markerWidth="8" markerHeight="8" orient="auto" markerUnits="userSpaceOnUse">
      <path d="M1 1 L9 5 L1 9" fill="none" stroke="#222" stroke-width="1.4"/>
    </marker>
    <symbol id="star" viewBox="0 0 20 20">
      <path d="M10 1 L12.6 7.1 L19.2 7.6 L14.2 11.9 L15.7 18.4 L10 15 L4.3 18.4 L5.8 11.9 L0.8 7.6 L7.4 7.1 Z"/>
    </symbol>
    <symbol id="db" viewBox="0 0 40 50">
      <ellipse cx="20" cy="8" rx="18" ry="6"/>
      <path d="M2 12 v8 a18 6 0 0 0 36 0 v-8 a18 6 0 0 1 -36 0z"/>
      <path d="M2 24 v8 a18 6 0 0 0 36 0 v-8 a18 6 0 0 1 -36 0z"/>
      <path d="M2 36 v6 a18 6 0 0 0 36 0 v-6 a18 6 0 0 1 -36 0z"/>
    </symbol>
    <symbol id="lock-badge" viewBox="0 0 24 24">
      <circle cx="12" cy="12" r="11" fill="#fff" stroke="#6b3fa0" stroke-width="2"/>
      <rect x="7" y="11" width="10" height="8" rx="1" fill="#6b3fa0"/>
      <path d="M9 11 v-3 a3 3 0 0 1 6 0 v3" fill="none" stroke="#6b3fa0" stroke-width="2"/>
    </symbol>
  </defs>

  <!-- Heading -->
  <text class="chart-title" x="600" y="68" text-anchor="middle">Data Flow Chart</text>
  <line class="title-rule" x1="221" y1="80" x2="974" y2="80"/>

  <!-- 1. Data collection -->
  <text class="label" x="26" y="108"><tspan class="step-num">1.</tspan> Data Collection</text>

  <rect class="fill-purple" x="50" y="115" width="30" height="42" rx="8" role="img" aria-label="Contractor worker figure in hard hat"/>
  <text class="caption" x="29" y="172">Contractors</text>
  <rect class="fill-purple" x="50" y="177" width="30" height="42" rx="8" role="img" aria-label="Subcontractor worker figure in hard hat"/>
  <text class="caption" x="17" y="232">SubContractors</text>
  <rect class="fill-purple" x="50" y="238" width="30" height="42" rx="8" role="img" aria-label="Third party data feed figure in hard hat"/>
  <text class="caption" x="29" y="296">Third Party</text>
  <text class="caption" x="29" y="314">Data Feeds</text>

  <line class="flow-solid" x1="80" y1="152" x2="188" y2="178" marker-end="url(#tip)"/>
  <line class="flow-solid" x1="82" y1="198" x2="186" y2="198" marker-end="url(#tip)"/>
  <line class="flow-solid" x1="80" y1="270" x2="192" y2="217" marker-end="url(#tip)"/>

  <text class="label" x="197" y="133">Uploaded in</text>
  <text class="label" x="197" y="154">our website</text>
  <g class="website-icon">
    <circle class="stroke-blue" cx="223" cy="195" r="31" stroke-width="4"/>
    <ellipse class="stroke-blue" cx="223" cy="195" rx="13" ry="31" stroke-width="3.5"/>
    <line class="stroke-blue" x1="223" y1="164" x2="223" y2="226" stroke-width="3.5"/>
    <line class="stroke-blue" x1="192" y1="195" x2="254" y2="195" stroke-width="3.5"/>
    <path class="stroke-blue" d="M197 179 h52 M197 211 h52" stroke-width="3"/>
    <rect x="258" y="185" width="70" height="19" rx="9.5" fill="#fff" stroke="#37a9dd" stroke-width="3"/>
    <text x="289" y="200" text-anchor="middle" font-size="15" font-weight="600" fill="#222">www</text>
  </g>

  <line class="flow-dash" x1="335" y1="194" x2="414" y2="194" marker-end="url(#chevron)"/>

  <text class="label" x="412" y="161">Data Base</text>
  <use href="#db" x="423" y="169" width="36" height="56" class="fill-blue"/>
  <use href="#lock-badge" x="443" y="203" width="24" height="24"/>
  <text class="caption" x="403" y="246">Data Stored Securely</text>
  <text class="caption" x="403" y="265">in Data Base</text>

  <line class="flow-dash" x1="485" y1="192" x2="563" y2="192" marker-end="url(#chevron)"/>

  <!-- 2. Cleansing & merging -->
  <text class="label" x="561" y="146"><tspan class="step-num">2.</tspan>Data Cleansing and</text>
  <text class="label" x="576" y="164">Merging</text>
  <use href="#db" x="578" y="171" width="34" height="42" class="fill-purple"/>
  <path d="M624 175 L606 200" stroke="#37a9dd" stroke-width="3"/>
  <path d="M600 196 L612 204 L606 214 L592 208 Z" fill="#37a9dd"/>
  <circle cx="620" cy="210" r="2" fill="#37a9dd"/>
  <circle cx="627" cy="206" r="1.6" fill="#37a9dd"/>
  <use href="#db" x="634" y="169" width="34" height="42" class="fill-purple"/>
  <circle cx="667" cy="200" r="11" fill="#fff" stroke="#37a9dd" stroke-width="2.5"/>
  <path d="M667 193 v14 M660 200 h14" stroke="#37a9dd" stroke-width="2.5"/>

  <line class="flow-dash" x1="693" y1="189" x2="771" y2="189" marker-end="url(#chevron)"/>

  <!-- 3. Data prep -->
  <text class="label" x="759" y="138"><tspan class="step-num">3.</tspan> Data Prep/Ratio Calculation</text>
  <use href="#db" x="771" y="204" width="32" height="38" class="fill-purple"/>
  <use href="#lock-badge" x="792" y="223" width="20" height="20"/>
  <path class="stroke-blue" d="M832 168 a50 38 0 0 1 60 -18" stroke-width="2.2" marker-end="url(#tip)"/>
  <path class="stroke-purple" d="M908 225 a50 38 0 0 1 -60 12" stroke-width="2.2" marker-end="url(#tip)"/>
  <rect x="818" y="172" width="30" height="44" fill="#fff" stroke="#37a9dd" stroke-width="2"/>
  <path d="M823 180 h20 M823 186 h20 M823 192 h20 M823 198 h20 M823 204 h14" stroke="#37a9dd" stroke-width="1.8"/>
  <path d="M808 200 h10" stroke="#37a9dd" stroke-width="2" marker-end="url(#tip)"/>
  <rect x="890" y="163" width="32" height="46" fill="#fff" stroke="#6b3fa0" stroke-width="2"/>
  <rect x="884" y="168" width="32" height="46" fill="#fff" stroke="#6b3fa0" stroke-width="2"/>
  <path d="M889 176 h22 M889 182 h22 M889 188 h22 M889 194 h22 M889 200 h16" stroke="#6b3fa0" stroke-width="1.8"/>
  <path d="M898 206 L930 226" stroke="#6b3fa0" stroke-width="4" stroke-linecap="round"/>
  <text class="caption" x="760" y="259">Data is manipulated &amp; prepared for</text>
  <text class="caption" x="760" y="278">a run through Financial Model</text>

  <path class="flow-dash" d="M944 189 H1078 V288" marker-end="url(#chevron)"/>

  <!-- 4. Model run -->
  <text class="label" x="996" y="318"><tspan class="step-num">4.</tspan>Model Run / Scoring</text>
  <g class="gauge">
    <path d="M1025 401 A50 50 0 0 1 1034 346" stroke="#6b3fa0" stroke-width="18" fill="none"/>
    <path d="M1037 342 A50 50 0 0 1 1066 331" stroke="#8a66bb" stroke-width="18" fill="none"/>
    <path d="M1070 331 A50 50 0 0 1 1102 343" stroke="#6b3fa0" stroke-width="18" fill="none"/>
    <path d="M1105 346 A50 50 0 0 1 1117 401" stroke="#37a9dd" stroke-width="18" fill="none"/>
    <path d="M1067 391 L1085 348 L1075 393 Z" fill="#4d2a7c"/>
    <circle cx="1071" cy="390" r="6" fill="#8a66bb"/>
  </g>
  <text class="caption" x="961" y="416">“ Scoring / grading ” of Contractors</text>

  <line class="flow-dash" x1="1071" y1="426" x2="1071" y2="504" marker-end="url(#chevron)"/>

  <!-- 5a. Paying users -->
  <text class="label" x="970" y="524"><tspan class="step-num">5a.</tspan>Dashboard - Paying Users</text>
  <rect x="1022" y="544" width="99" height="75" rx="6" fill="url(#moneyTone)" role="img" aria-label="Hand holding a dollar banknote"/>
  <defs>
    <linearGradient id="moneyTone" x1="0" y1="1" x2="1" y2="0">
      <stop offset="0" stop-color="#37a9dd"/>
      <stop offset="1" stop-color="#6b3fa0"/>
    </linearGradient>
  </defs>
  <text class="caption" x="974" y="634">“ Score / grade ” availaable for</text>
  <text class="caption" x="974" y="653">Paying Users to see</text>

  <path class="flow-dash" d="M1078 665 V716 H823" marker-end="url(#chevron)"/>

  <!-- 5b. Contractor dashboard -->
  <text class="label" x="600" y="605"><tspan class="step-num">5b.</tspan> Dashboard - contractors</text>
  <text class="caption" x="628" y="630">[ Log in ]  Contractors</text>

  <g class="rank-rows">
    <rect class="fill-purple" x="616" y="642" width="14" height="22" rx="4" role="img" aria-label="Contractor figure"/>
    <rect class="fill-purple" x="616" y="674" width="14" height="22" rx="4" role="img" aria-label="Contractor figure"/>
    <rect class="fill-purple" x="616" y="699" width="14" height="22" rx="4" role="img" aria-label="Contractor figure"/>
    <rect class="fill-purple" x="616" y="729" width="14" height="22" rx="4" role="img" aria-label="Contractor figure"/>

    <use href="#star" class="star-on" x="640" y="644" width="20" height="20"/>
    <use href="#star" class="star-on" x="666" y="644" width="20" height="20"/>
    <use href="#star" class="star-on" x="692" y="644" width="20" height="20"/>
    <use href="#star" class="star-off" x="718" y="644" width="20" height="20"/>
    <use href="#star" class="star-off" x="744" y="644" width="20" height="20"/>
    <use href="#star" class="star-off" x="770" y="644" width="20" height="20"/>

    <use href="#star" class="star-on" x="640" y="676" width="20" height="20"/>
    <use href="#star" class="star-off" x="666" y="676" width="20" height="20"/>
    <use href="#star" class="star-off" x="692" y="676" width="20" height="20"/>
    <use href="#star" class="star-off" x="718" y="676" width="20" height="20"/>
    <use href="#star" class="star-off" x="744" y="676" width="20" height="20"/>
    <use href="#star" class="star-off" x="770" y="676" width="20" height="20"/>

    <use href="#star" class="star-on" x="640" y="701" width="20" height="20"/>
    <use href="#star" class="star-on" x="666" y="701" width="20" height="20"/>
    <use href="#star" class="star-on" x="692" y="701" width="20" height="20"/>
    <use href="#star" class="star-on" x="718" y="701" width="20" height="20"/>
    <use href="#star" class="star-on" x="744" y="701" width="20" height="20"/>
    <use href="#star" class="star-off" x="770" y="701" width="20" height="20"/>

    <use href="#star" class="star-on" x="640" y="731" width="20" height="20"/>
    <use href="#star" class="star-on" x="666" y="731" width="20" height="20"/>
    <use href="#star" class="star-on" x="692" y="731" width="20" height="20"/>
    <use href="#star" class="star-on" x="718" y="731" width="20" height="20"/>
    <use href="#star" class="star-off" x="744" y="731" width="20" height="20"/>
    <use href="#star" class="star-off" x="770" y="731" width="20" height="20"/>
  </g>

  <line class="flow-dash" x1="589" y1="686" x2="510" y2="686" marker-end="url(#chevron)"/>

  <!-- 6. Project review -->
  <text class="label" x="158" y="630"><tspan class="step-num">6.</tspan> Contractor project  review</text>
  <text class="label" x="178" y="646">information Uploaded in the</text>
  <text class="label" x="175" y="662">Dashboard/interface</text>
  <g class="review-doc">
    <path d="M384 606 H494 V752 H408 L384 728 Z" fill="#fff" stroke="#6b3fa0" stroke-width="2"/>
    <path d="M384 728 H408 V752 Z" fill="#4d2a7c"/>
    <rect class="fill-purple" x="391" y="613" width="32" height="45" rx="6" role="img" aria-label="Contractor figure"/>
    <line class="doc-line" x1="430" y1="624" x2="484" y2="624"/>
    <line class="doc-line" x1="430" y1="638" x2="484" y2="638"/>
    <line class="doc-line" x1="430" y1="652" x2="484" y2="652"/>
    <line class="doc-line" x1="394" y1="670" x2="484" y2="670"/>
    <line class="doc-line" x1="394" y1="684" x2="484" y2="684"/>
    <line class="doc-line" x1="394" y1="698" x2="484" y2="698"/>
    <line class="doc-line" x1="394" y1="712" x2="434" y2="712"/>
  </g>

  <!-- 7. Machine learning -->
  <rect class="ml-frame" x="531" y="294" width="273" height="241" rx="35"/>
  <path class="fill-blue" d="M632 367 a18 18 0 0 1 8 -32 a30 30 0 0 1 56 -10 a22 22 0 0 1 30 24 a16 16 0 0 1 -4 18 Z"/>
  <line class="flow-solid" x1="678" y1="375" x2="678" y2="400" stroke-width="1.6" marker-end="url(#tip)" marker-start="url(#tip)"/>
  <path d="M576 418 V403 H766 V418" fill="none" stroke="#222" stroke-width="1.2"/>
  <rect x="576" y="410" width="174" height="71" rx="4" fill="url(#mlTone)" role="img" aria-label="Hands typing on a laptop beside a phone and tablet"/>
  <defs>
    <linearGradient id="mlTone" x1="0" y1="0" x2="1" y2="1">
      <stop offset="0" stop-color="#8a66bb"/>
      <stop offset="1" stop-color="#6b3fa0"/>
    </linearGradient>
  </defs>
  <text class="label" x="560" y="502"><tspan class="step-num">7.</tspan>Machine Learning / Artificial</text>
  <text class="label" x="575" y="523">Intelligence</text>

  <line class="flow-dash" x1="810" y1="335" x2="868" y2="291" marker-end="url(#chevron)" marker-start="url(#chevron)"/>
  <line class="flow-dash" x1="810" y1="416" x2="1009" y2="352" marker-end="url(#chevron)" marker-start="url(#chevron)"/>
</svg>
</body>
</html>
```